Design some Business Cards for Skyquill Studio

I would like some business cards made for my Aerial Photography business.
Logo, contact details social media sites and maybe some catch phrase

facebook.com/skyquillstudiotq
youtube.com/skyquillstudio
instagram.com/skyquillstudio
http://www.skyquillstudiotq.example

```html
<!DOCTYPE html>
<html lang="en">
<head>
<meta charset="utf-8">
<title>Skyquill Studio – Business Cards</title>
<link rel="stylesheet" href="https://fonts.googleapis.com/css2?family=Questrial&display=swap">
<style>
  :root {
    --page: #e9e6e1;
    --card-black: #0d0d0e;
    --card-black-edge: #1f1f22;
    --card-white: #ffffff;
    --brand-blue: #2a8fc0;
    --text-white: #f2f2f2;
    --text-grey: #b9b9b9;
    --text-dark: #2a2a2a;
    --name-box: #2b2b2e;
  }
  * { box-sizing: border-box; margin: 0; padding: 0; }
  html, body {
    width: 1200px; height: 912px; overflow: hidden;
    background: var(--page);
    font-family: "Questrial", "Century Gothic", sans-serif;
  }
  .canvas { position: relative; width: 1200px; height: 912px; }

  .card {
    position: absolute;
    width: 540px; height: 308px;
    border-radius: 4px;
    overflow: hidden;
    box-shadow: 0 14px 30px rgba(0,0,0,.28);
  }

  /* front */
  .card-front {
    left: 70px; top: 110px;
    background: linear-gradient(135deg, var(--card-black-edge), var(--card-black) 55%);
    display: flex; flex-direction: column; align-items: center; justify-content: center;
  }
  .brand { display: flex; align-items: center; gap: 14px; }
  .brand-dot {
    width: 34px; height: 34px; border-radius: 50%;
    background: var(--brand-blue);
  }
  .brand-name {
    color: var(--brand-blue);
    font-size: 34px; letter-spacing: .5px;
  }
  .front-url {
    margin-top: 44px;
    color: var(--text-grey);
    font-size: 15px; letter-spacing: 5px;
  }

  /* back */
  .card-back {
    left: 590px; top: 500px;
    display: flex;
    background: var(--card-white);
  }
  .back-brand-panel {
    width: 46%;
    background: linear-gradient(135deg, var(--card-black-edge), var(--card-black) 60%);
    display: flex; align-items: center; justify-content: center;
  }
  .back-brand-panel .brand { gap: 9px; }
  .back-brand-panel .brand-dot { width: 24px; height: 24px; }
  .back-brand-panel .brand-name { font-size: 22px; }

  .back-details {
    flex: 1;
    padding: 34px 0 0 0;
    display: flex; flex-direction: column; align-items: flex-end;
  }
  .name-box {
    width: 92%;
    background: var(--name-box);
    border-radius: 10px 0 0 10px;
    padding: 12px 22px 10px 24px;
    color: var(--text-white);
  }
  .person-name { font-size: 26px; letter-spacing: 1px; }
  .person-role { font-size: 15px; text-align: right; margin-top: 2px; letter-spacing: 1px; }

  .contact-list {
    list-style: none;
    align-self: flex-start;
    margin: 34px 0 0 30px;
  }
  .contact-list li {
    display: flex; align-items: center; gap: 10px;
    color: var(--text-dark);
    font-size: 13px; line-height: 22px;
  }
  .contact-list li::before {
    content: ""; width: 7px; height: 7px; border-radius: 50%;
    background: var(--text-dark);
  }
</style>
</head>
<body>
<main class="canvas">
  <section class="card card-front" aria-label="Business card front">
    <div class="brand">
      <span class="brand-dot"></span>
      <span class="brand-name">skyquillstudio</span>
    </div>
    <p class="front-url">www.skyquillstudiotq.example</p>
  </section>

  <section class="card card-back" aria-label="Business card back">
    <div class="back-brand-panel">
      <div class="brand">
        <span class="brand-dot"></span>
        <span class="brand-name">skyquillstudio</span>
      </div>
    </div>
    <div class="back-details">
      <div class="name-box">
        <p class="person-name">MARA LIND</p>
        <p class="person-role">C.E.O</p>
      </div>
      <ul class="contact-list">
        <li>facebook.com/skyquillstudiotq</li>
        <li>http://www.skyquillstudiotq.example</li>
        <li>instagram.com/skyquillstudio</li>
        <li>youtube.com/skyquillstudio</li>
      </ul>
    </div>
  </section>
</main>
</body>
</html>
```